Premium Food Label Design – High-End Boutique Jar Labels (3 Sizes)

I require a complete jar label redesign across three sizes:
75mm x 130mm (Large & Medium)
55mm x 120mm (Small)
45mm x 120mm (XS)

The design must feel professional, modern, elegant, and high-end boutique.
Primary aesthetic: white, minimal, refined, with accents in soft brown and gold/bronze. (see prefer colours of logo in OLD LABEL PDF)
Transparent background required.

I have attached my current label for wording reference only — I want to move away from the kraft look entirely.
The label must include all existing details, plus a dedicated space to manually add batch number and date.

IMPORTANT: Final files must be supplied as editable Adobe Illustrator (.AI) files with live text layers (not outlined) so I can update them as needed.
Logo is attached. I’m open to a fresh, elevated design direction aligned with a premium brand feel.
Updates

Low design quality

Target Market(s)

People who appreciate high-end, thoughtfully crafted food and are willing to pay for quality

Industry/Entity Type

Gourmet Food / Artisan Food Packaging

Requirements
Must have
• Premium, minimal aesthetic, Strong typography hierarchy, White background, Consistency across 3 sizes
Nice to have
• Elevated “Amber Meadow” styling
Should not have
• No bright or bold colours, No clutter or overcrowding, No heavy borders or thick frames,No “homemade/craft” fonts

```html
<!DOCTYPE html>
<html lang="en">
<head>
<meta charset="utf-8">
<title>Hearth &amp; Grove – Jar Label Concepts</title>
<link rel="stylesheet" href="https://fonts.googleapis.com/css2?family=Poppins:wght@400;700&family=Libre+Caslon+Text:ital,wght@0,400;0,700;1,400&family=Lato:wght@400;700&family=Great+Vibes&family=Roboto+Condensed:wght@400;500&display=swap">
<style>
:root{
  --red:#e8112d;
  --brown:#4a2a17;
  --brown-dark:#3b2214;
  --gold:#b58a4c;
  --gold-soft:#d4b58a;
  --ink:#2b2420;
  --paper:#f6f4ef;
  --label:#fbfaf7;
  --panel:#efefef;
  --scene:#eeebe4;
  --black:#111;
}
*{margin:0;padding:0;box-sizing:border-box}
html,body{width:684px;height:1200px;overflow:hidden;background:#fff}
body{position:relative;font-family:'Lato',sans-serif;color:var(--ink)}
.abs{position:absolute}
.concept-title{position:absolute;font-family:'Poppins',sans-serif;font-size:17px;color:var(--red);white-space:nowrap}
.concept-title b{font-weight:700}
.concept-title span{font-weight:400}
.serif{font-family:'Libre Caslon Text',serif}
.script{font-family:'Great Vibes',cursive}
.cond{font-family:'Roboto Condensed',sans-serif}
.center{text-align:center}

/* Concept 1 */
.c1-front{left:165px;top:90px;width:201px;height:303px;background:var(--paper);border-radius:6px}
.c1-front .frame{position:absolute;inset:8px;border:1px solid var(--gold-soft)}
.c1-back{left:385px;top:90px;width:128px;height:303px;background:var(--paper);border-radius:6px;overflow:hidden}
.tag-vertical{position:absolute;transform:rotate(-90deg);transform-origin:left top;white-space:nowrap;letter-spacing:1px;font-weight:700}
.brand-small{font-family:'Libre Caslon Text',serif;letter-spacing:2px;white-space:nowrap}
.product-title{font-family:'Libre Caslon Text',serif;font-weight:700;line-height:1;color:var(--ink);white-space:nowrap}
.rule{position:absolute;height:1px;background:var(--gold)}
.mark-circle{position:absolute;border-radius:50%;background:var(--gold)}
.contact-band{position:absolute;left:0;right:0;bottom:0;color:#fff;font-size:6.5px;line-height:1.35;text-align:center;white-space:nowrap}

/* Concept 2 */
.c2-panel{left:61px;top:448px;width:502px;height:348px;background:var(--panel)}
.c2-label{position:absolute;background:var(--label);border:1px solid var(--gold-soft)}

/* Concept 3 */
.c3-panel{left:61px;top:854px;width:569px;height:296px;background:var(--scene)}
.c3-label{position:absolute;background:rgba(255,255,255,.6);border:1px solid #c9c2b6;text-align:center;color:#333}
.c3-brand{font-family:'Roboto Condensed',sans-serif;font-weight:500;color:var(--gold);line-height:1}
.c3-fine{font-size:5px;line-height:1.35}
.batch-box{position:absolute;border:1px solid #aaa;text-align:left;font-size:5.5px;line-height:1.5;padding:2px 3px}
</style>
</head>
<body>

<!-- CONCEPT 1 -->
<div class="concept-title" style="left:162px;top:50px"><b>CONCEPT - 1</b> <span>(TRANSPARENT LABEL)</span></div>

<section class="abs c1-front" aria-label="Front label">
  <div class="frame"></div>
  <div class="rule" style="left:20px;top:15px;width:1px;height:140px;background:var(--gold-soft)"></div>
  <div class="tag-vertical" style="left:15px;top:142px;font-size:9.5px;color:var(--ink)">POPULAR CHOICE</div>
  <div class="abs brand-small center" style="left:36px;top:34px;width:150px;font-size:10.5px">HEARTH &amp; GROVE</div>
  <div class="rule" style="left:48px;top:50px;width:128px"></div>
  <div class="abs product-title center" style="left:36px;top:58px;width:150px;font-size:27px">TOMATO<br>RELISH</div>
  <div class="rule" style="left:48px;top:124px;width:128px"></div>
  <div class="mark-circle" style="left:85px;top:175px;width:52px;height:52px;background:var(--brown)"></div>
  <div class="abs brand-small center" style="left:36px;top:238px;width:150px;font-size:11px;color:var(--gold)">HEARTH &amp; GROVE</div>
  <div class="abs script" style="left:52px;top:256px;font-size:19px;color:var(--ink)">Made with love <span style="color:var(--brown)">♥</span></div>
  <div class="abs" style="right:16px;top:276px;font-size:11px">375g</div>
</section>

<section class="abs c1-back" aria-label="Back label">
  <div class="abs serif center" style="left:0;top:14px;width:128px;font-size:15px;font-style:italic">Amber Meadow</div>
  <div class="rule" style="left:10px;top:34px;width:108px"></div>
  <p class="abs center" style="left:8px;top:42px;width:112px;font-size:9.5px;line-height:1.35">What is made with love is felt in return. May this relish nourish more than the meal—bringing comfort, connection, and joy to every moment shared.</p>
  <svg class="abs" style="left:52px;top:146px" width="24" height="22" viewBox="0 0 24 22" aria-hidden="true"><path d="M12 21 C4 14 0 10 0 6 A6 6 0 0 1 12 4 A6 6 0 0 1 24 6 C24 10 20 14 12 21Z" fill="var(--brown-dark)"/></svg>
  <div class="rule" style="left:10px;top:172px;width:108px"></div>
  <p class="abs center" style="left:6px;top:178px;width:116px;font-size:8.5px;line-height:1.35">Ingredients: Tomatoes, onion, sugar, vinegar, salt, spices, thickener (cornflour)</p>
  <div class="rule" style="left:10px;top:218px;width:108px"></div>
  <p class="abs serif center" style="left:6px;top:222px;width:116px;font-size:6.5px;font-style:italic;line-height:1.4">STORAGE: KEEP REFRIGERATED ONCE OPENED.</p>
  <div class="rule" style="left:10px;top:244px;width:108px"></div>
  <div class="abs" style="left:9px;top:252px;font-size:7.5px">Batch # ______ Date: ______</div>
  <div class="contact-band" style="height:34px;background:var(--brown-dark);padding-top:4px;font-size:6px">Made by Hearth &amp; Grove, QLD, Australia<br>W: hearthandgrove.com | E:<br>hello@hearthandgrove.com</div>
</section>

<!-- CONCEPT 2 -->
<div class="concept-title" style="left:61px;top:422px"><b>CONCEPT - 2</b> <span>(TRANSPARENT LABEL)</span></div>
<div class="abs c2-panel"></div>

<section class="c2-label" style="left:90px;top:530px;width:132px;height:218px" aria-label="Front label">
  <div class="abs" style="left:5px;top:8px;width:14px;height:98px;border:1px solid var(--gold-soft)"></div>
  <div class="tag-vertical" style="left:6px;top:100px;font-size:7.5px">POPULAR CHOICE</div>
  <div class="abs product-title center" style="left:22px;top:14px;width:106px;font-size:18px">TOMATO<br>RELISH</div>
  <div class="mark-circle" style="left:58px;top:90px;width:38px;height:38px"></div>
  <div class="abs brand-small center" style="left:22px;top:134px;width:106px;font-size:8px">HEARTH &amp; GROVE</div>
  <div class="abs script" style="left:34px;top:158px;font-size:14px">Made with love <span style="color:var(--gold)">♥</span></div>
  <div class="abs serif" style="left:42px;top:190px;font-size:8px">Net Weight 375g</div>
</section>

<section class="c2-label" style="left:262px;top:535px;width:132px;height:210px;overflow:hidden" aria-label="Front label with batch">
  <div class="abs" style="left:5px;top:8px;width:14px;height:94px;border:1px solid var(--gold-soft)"></div>
  <div class="tag-vertical" style="left:6px;top:96px;font-size:7.5px">POPULAR CHOICE</div>
  <div class="abs product-title center" style="left:22px;top:12px;width:106px;font-size:17px">TOMATO<br>RELISH</div>
  <div class="mark-circle" style="left:60px;top:82px;width:34px;height:34px"></div>
  <div class="abs brand-small center" style="left:22px;top:120px;width:106px;font-size:8px">HEARTH &amp; GROVE</div>
  <div class="abs script" style="left:38px;top:140px;font-size:13px">Made with love <span style="color:var(--gold)">♥</span></div>
  <div class="abs" style="left:8px;top:164px;font-size:7px">Batch No: _____ Date: _____</div>
  <div class="contact-band serif" style="height:30px;background:var(--black);padding-top:4px;font-size:5.5px">Made by Hearth &amp; Grove, QLD, Australia<br>W: hearthandgrove.com E:<br>hello@hearthandgrove.com</div>
</section>

<section class="c2-label" style="left:432px;top:543px;width:98px;height:202px;overflow:hidden" aria-label="Back label">
  <p class="abs center" style="left:5px;top:6px;width:88px;font-size:7.5px;line-height:1.35">Amber Meadow<br>What is made with love is felt in return.<br>May this relish nourish more than the meal—bringing comfort, connection, and joy<br>to every moment shared.</p>
  <div class="rule" style="left:8px;top:104px;width:82px"></div>
  <div class="mark-circle" style="left:43px;top:110px;width:12px;height:12px"></div>
  <p class="abs center" style="left:5px;top:127px;width:88px;font-size:7px;line-height:1.3">Ingredients: Tomatoes, onion, sugar, vinegar, salt, spices, thickener (cornflour)</p>
  <div class="abs" style="left:6px;top:160px;font-size:6.5px">Batch No: _____ Date: ____</div>
  <div class="contact-band serif" style="height:30px;background:var(--black);padding-top:4px;font-size:4.8px">Made by Hearth &amp; Grove, QLD, Australia<br>W: hearthandgrove.com E:<br>hello@hearthandgrove.com</div>
</section>

<!-- CONCEPT 3 -->
<div class="concept-title" style="left:61px;top:828px"><b>CONCEPT - 3</b> <span>(TRANSPARENT LABEL)</span></div>
<div class="abs c3-panel"></div>

<section class="c3-label" style="left:146px;top:916px;width:160px;height:214px" aria-label="Chai spice blend label">
  <div class="abs c3-brand center" style="left:0;top:16px;width:100%;font-size:17px">HEARTH &amp; GROVE</div>
  <div class="abs cond center" style="left:0;top:62px;width:100%;font-size:14px">CHAI SPICE BLEND</div>
  <div class="abs center" style="left:0;top:80px;width:100%;font-size:6.5px">Net Wt. 200g</div>
  <div class="abs center" style="left:0;top:96px;width:100%;font-size:7.5px">Botanical Harmony</div>
  <p class="abs c3-fine center" style="left:8px;top:108px;width:144px">A carefully curated blend of single-origin spices and organic botanicals. Intentional, serene, and full of soul. A modern apothecary interpretation of ancient wellness.</p>
  <p class="abs c3-fine center" style="left:8px;top:136px;width:144px">Ingredients: Single-origin Cardamom, Ceylon Cinnamon, Ginger, Cloves, Star Anise, Thyme. All ingredients organic.<br>Origin: Sri Lanka, India. Packaged in England.</p>
  <div class="batch-box" style="left:8px;top:174px;width:112px;height:22px">BATCH No:<br>DATE:</div>
  <div class="abs center" style="left:0;top:203px;width:100%;font-size:4.5px">www.hearthandgrove.com | @hearthandgrovefood</div>
</section>

<section class="c3-label" style="left:353px;top:950px;width:95px;height:178px" aria-label="Rosemary truffle salt label">
  <div class="abs c3-brand center" style="left:0;top:14px;width:100%;font-size:11px">HEARTH &amp; GROVE</div>
  <div class="abs cond center" style="left:0;top:52px;width:100%;font-size:10px;line-height:1.1">ROSEMARY<br>TRUFFLE SALT</div>
  <div class="abs center" style="left:0;top:78px;width:100%;font-size:5px">Net Wt. 120g</div>
  <p class="abs c3-fine center" style="left:6px;top:88px;width:83px">A premium blend of sea salt, black truffle and dried organic rosemary for mindful cooking.</p>
  <p class="abs c3-fine center" style="left:6px;top:110px;width:83px">Ingredients: Sea salt, truffle, rosemary. Origin: Sri Lanka, India.</p>
  <div class="batch-box" style="left:6px;top:134px;width:70px;height:20px">BATCH No:<br>DATE:</div>
  <div class="abs center" style="left:0;top:164px;width:100%;font-size:4px">hearthandgrove.com | @hearthandgrovefood</div>
</section>

<section class="c3-label" style="left:493px;top:986px;width:69px;height:136px" aria-label="Finishing chili garlic oil label">
  <div class="abs c3-brand center" style="left:0;top:10px;width:100%;font-size:8.5px">HEARTH &amp;<br>GROVE</div>
  <div class="abs cond center" style="left:0;top:36px;width:100%;font-size:7.5px;line-height:1.1">FINISHING<br>CHILI-GARLIC OIL</div>
  <div class="abs center" style="left:0;top:56px;width:100%;font-size:4.5px">Net Wt. 80g</div>
  <p class="abs c3-fine center" style="left:4px;top:64px;width:61px;font-size:4.5px">A balanced small-batch oil infused with sun-dried chili and garlic.</p>
  <p class="abs c3-fine center" style="left:4px;top:84px;width:61px;font-size:4.5px">Ingredients: Olive oil, chili, garlic, thyme.</p>
  <div class="batch-box" style="left:4px;top:102px;width:50px;height:17px;font-size:4.5px">BATCH No:<br>DATE:</div>
  <div class="abs center" style="left:0;top:124px;width:100%;font-size:3.5px">hearthandgrove.com</div>
</section>

</body>
</html>
```